Stationery Design Project

We need a Stationery Design for automotive industry.
Updates

Target Market(s)

Mechanic garage and Mechanics

Industry/Entity Type

Automotive

Requirements
Must have
• The logo company and the legal information.

We are a car spart parts and tools delar
Nice to have
• We like something elegant and simple.
Should not have

```html
<!DOCTYPE html>
<html lang="en">
<head>
<meta charset="utf-8">
<title>Velora Motor Parts — Stationery Set</title>
<link rel="stylesheet" href="https://fonts.googleapis.com/css2?family=Arimo:ital,wght@0,400;0,700;1,400&display=swap">
<style>
  :root {
    --canvas: #38383a;
    --paper: #ffffff;
    --ink-black: #000000;
    --art-grey: #505054;
    --art-blue: #2f4a80;
    --art-dark: #161618;
    --link-blue: #4a78cc;
    --mark-grey: #6f6f72;
    --text-white: #ffffff;
    --window-line: #333333;
    --rim-light: #f4f4f4;
    --rim-dark: #9a9a9e;
  }
  html, body {
    margin: 0;
    padding: 0;
    width: 1200px;
    height: 1100px;
    overflow: hidden;
    background: var(--canvas);
  }
  .stationery-set {
    position: relative;
    width: 1200px;
    height: 1100px;
    background: var(--canvas);
    font-family: "Arimo", Arial, sans-serif;
  }
  .piece { position: absolute; display: block; }
  .letterhead {
    left: 358px; top: 73px; width: 700px; height: 990px;
    background: var(--paper);
  }
  .letterhead-header { position: absolute; left: 0; top: 0; width: 700px; height: 101px; }
  .envelope { left: 47px; top: 421px; width: 732px; height: 366px; }
  .disc { left: 786px; top: 225px; width: 414px; height: 414px; }
  .business-card { left: 286px; top: 822px; width: 300px; height: 166px; }

  .contact { font-family: "Arimo", Arial, sans-serif; font-style: italic; fill: var(--text-white); }
  .contact .web { fill: var(--link-blue); }
  .brand-name { font-family: "Arimo", Arial, sans-serif; font-weight: 400; fill: var(--mark-grey); letter-spacing: 1px; }
  .address-line { stroke: var(--window-line); stroke-width: 0.8; }
</style>
</head>
<body>
<main class="stationery-set">

  <!-- Letterhead -->
  <section class="piece letterhead" aria-label="Letterhead">
    <svg class="letterhead-header" viewBox="0 0 595 86" preserveAspectRatio="none">
      <defs>
        <linearGradient id="lh-art" x1="0" y1="0" x2="1" y2="0">
          <stop offset="0" stop-color="var(--art-dark)"/>
          <stop offset="0.55" stop-color="var(--ink-black)"/>
          <stop offset="0.85" stop-color="var(--art-dark)"/>
          <stop offset="0.93" stop-color="var(--art-blue)"/>
          <stop offset="1" stop-color="var(--art-grey)"/>
        </linearGradient>
      </defs>
      <rect class="header-artwork" width="595" height="86" fill="url(#lh-art)"
            role="img" aria-label="Decorative sweeping blue and grey band artwork"/>
      <text class="brand-name" x="175" y="47" text-anchor="middle" font-size="17">VELORA</text>
      <text class="brand-name" x="175" y="60" text-anchor="middle" font-size="6">MOTOR PARTS</text>
      <g class="contact" font-size="7.5" text-anchor="end">
        <text x="512" y="25">Country, City, Street 12</text>
        <text x="513" y="38">Phone: 123.456.7890</text>
        <text x="517" y="51">Fax: 456.7890</text>
        <text x="520" y="64">E-mail: companyname@mail.com</text>
        <text class="web" x="522" y="77">www.companyname.com</text>
      </g>
    </svg>
  </section>

  <!-- Envelope -->
  <svg class="piece envelope" viewBox="0 0 623 312" preserveAspectRatio="none" aria-label="Envelope">
    <defs>
      <linearGradient id="env-art" x1="0" y1="0" x2="1" y2="0.4">
        <stop offset="0" stop-color="var(--art-grey)"/>
        <stop offset="0.1" stop-color="var(--art-blue)"/>
        <stop offset="0.3" stop-color="var(--ink-black)"/>
        <stop offset="0.75" stop-color="var(--ink-black)"/>
        <stop offset="1" stop-color="var(--art-dark)"/>
      </linearGradient>
    </defs>
    <rect class="envelope-artwork" width="623" height="312" fill="url(#env-art)"
          role="img" aria-label="Decorative sweeping blue and grey band artwork"/>
    <text class="brand-name" x="550" y="80" text-anchor="middle" font-size="22">VELORA</text>
    <text class="brand-name" x="550" y="92" text-anchor="middle" font-size="7">MOTOR PARTS</text>
    <g class="contact" font-size="8.5">
      <text x="75" y="127">Country, City, Street 12</text>
      <text x="89" y="140">Phone: 123.456.7890</text>
      <text x="97" y="154">Fax: 456.7890</text>
      <text x="105" y="166">E-mail: companyname@mail.com</text>
      <text class="web" x="118" y="181">www.companyname.com</text>
    </g>
    <rect x="265" y="160" width="329" height="122" rx="10" fill="var(--paper)"/>
    <g class="address-lines">
      <line class="address-line" x1="286" y1="188" x2="575" y2="188"/>
      <line class="address-line" x1="286" y1="207" x2="575" y2="207"/>
      <line class="address-line" x1="286" y1="227" x2="575" y2="227"/>
      <line class="address-line" x1="286" y1="246" x2="575" y2="246"/>
      <line class="address-line" x1="286" y1="265" x2="575" y2="265"/>
    </g>
  </svg>

  <!-- Disc -->
  <svg class="piece disc" viewBox="0 0 352 352" aria-label="Disc label">
    <defs>
      <linearGradient id="disc-rim" x1="0" y1="0" x2="1" y2="1">
        <stop offset="0" stop-color="var(--rim-light)"/>
        <stop offset="0.5" stop-color="var(--rim-dark)"/>
        <stop offset="1" stop-color="var(--rim-light)"/>
      </linearGradient>
      <linearGradient id="disc-art" x1="0" y1="0" x2="1" y2="1">
        <stop offset="0" stop-color="var(--art-dark)"/>
        <stop offset="0.35" stop-color="var(--ink-black)"/>
        <stop offset="0.7" stop-color="var(--ink-black)"/>
        <stop offset="0.88" stop-color="var(--art-blue)"/>
        <stop offset="1" stop-color="var(--art-grey)"/>
      </linearGradient>
      <radialGradient id="disc-hub" cx="0.4" cy="0.35" r="0.7">
        <stop offset="0" stop-color="#ffffff"/>
        <stop offset="0.6" stop-color="#cfcfd2"/>
        <stop offset="1" stop-color="#8e8e92"/>
      </radialGradient>
    </defs>
    <circle cx="168" cy="172" r="166" fill="url(#disc-rim)"/>
    <circle cx="168" cy="172" r="163" fill="var(--paper)"/>
    <circle class="disc-artwork" cx="168" cy="172" r="160" fill="url(#disc-art)"
            role="img" aria-label="Decorative sweeping blue and grey band artwork"/>
    <circle cx="168" cy="164" r="56" fill="url(#disc-hub)" stroke="#9a9a9e" stroke-width="1"/>
    <circle cx="168" cy="164" r="42" fill="none" stroke="#b5b5b8" stroke-width="3"/>
    <circle cx="168" cy="164" r="30" fill="#e8e8ea"/>
    <circle cx="168" cy="164" r="14" fill="var(--paper)" stroke="#aaaaad" stroke-width="1"/>
    <text class="brand-name" x="165" y="88" text-anchor="middle" font-size="15">VELORA</text>
    <text class="brand-name" x="165" y="97" text-anchor="middle" font-size="5">MOTOR PARTS</text>
    <g class="contact" font-size="7">
      <text x="145" y="250">Country, City, Street 12</text>
      <text x="162" y="261">Phone: 123.456.7890</text>
      <text x="174" y="272">Fax: 456.7890</text>
      <text class="web" x="188" y="285">www.companyname.com</text>
    </g>
  </svg>

  <!-- Business card -->
  <svg class="piece business-card" viewBox="0 0 255 141" preserveAspectRatio="none" aria-label="Business card">
    <defs>
      <linearGradient id="card-art" x1="0" y1="0" x2="1" y2="0.4">
        <stop offset="0" stop-color="var(--art-grey)"/>
        <stop offset="0.12" stop-color="var(--art-blue)"/>
        <stop offset="0.32" stop-color="var(--ink-black)"/>
        <stop offset="0.8" stop-color="var(--ink-black)"/>
        <stop offset="1" stop-color="var(--art-dark)"/>
      </linearGradient>
    </defs>
    <rect class="card-artwork" width="255" height="141" fill="url(#card-art)"
          role="img" aria-label="Decorative sweeping blue and grey band artwork"/>
    <text class="brand-name" x="180" y="44" text-anchor="middle" font-size="12">VELORA</text>
    <text class="brand-name" x="180" y="51" text-anchor="middle" font-size="4.5">MOTOR PARTS</text>
    <g class="contact" font-size="7.5">
      <text x="68" y="81">Country, City, Street 12</text>
      <text x="87" y="94">Phone: 123.456.7890</text>
      <text x="101" y="107">Fax: 456.7890</text>
      <text x="118" y="118">E-mail: companyname@mail.com</text>
      <text class="web" x="154" y="132">www.companyname.com</text>
    </g>
  </svg>

</main>
</body>
</html>
```